Timeless Estate Planning Law Firm Ad

We need an advertisement design for our Estate Planning Law Firm located in the Overland Park, Kansas. This ad will be placed in Brightwater Valley Civic College Stage Arts Playbill. Inside the front cover.

I want the ad "Pop" and be very clean. Not cluttered.

The final design should target the 55+ age demographic with upper income range. We want it to have a "Call to Action" to think about their own estate planning.

Target Market(s)

Industry/Entity Type

Lawyer

Font styles to use
Serif

Requirements
Must have
• Colors:
• Red: C5/M100/B25
• Gold: C20/M50/Y100/B42
• Black: C100/M100/Y100/B100
• Requirements:
• Ad size: 4.5"w x 7.5"h
• no bleed
• MATERIALS REQUIRED FOR PRINT PRODUCTS
• * PDF/X-1a files are required for all ads.
• * Fonts must be outlined or embedded.
• * All colors should be converted to CMYK (except black text).
• * Crop marks and color bars should be outside printable area (12-point offset).
• * Only one ad per PDF document.
• DOCUMENT SETUP
• Adobe InDesign for ad layouts.
• * Photoshop: 300 dpi CMYK or grayscale, 600 dpi minimum bitmap, flattened layers, TIF or EPS format, binary encoding (no JPG and no extra channels).
• * Illustrator: Outline all fonts, flatten transparencies, embed all elements (no links).
• * All fonts should be Type 1 or OpenType (Multiple Master Fonts are strongly discouraged).
• * All colors must be CMYK (except black text); no PMS/Pantone colors.
• * Ink density is not to exceed 300%.
• * Black text 12 points or smaller should be black only.
• (C=0%, M=0%, Y=0%, K=100%).
• * Reversed text must be a minimum of 10 points.
Nice to have
• Add Haldorsen Law Logo
• Attorney Picture: Milo T. Haldorsen
• Ideas for titles:
• Estate Planning: If You Don't Do It, The Court Will...
• We Will Be There When You Need Us...
• Let Us Help You
• * Avoid Probate and Court Interference with Your Affairs
• * Minimize Family In-fighting
• * Protect Heirs from Wasting Inheritances
• * Keep Assets in Your Bloodline
• * Preserve and Protect IRA's and Retirement Accounts
• List Our Services:
• Family Estate Planning, Trusts, Wills, Powers of Attorney, Business Succession Planning, Probate & Trust Administration, Asset Protection Planning, Special Needs Planning
• Include our:
• Get Your Estate Plan Done Today
• Free Consultation
• (555) 406-7319
• address: 4820 Pinecrest Avenue Suite 310 Overland Park, KS 66000
• website: (555) 406-7319
• Licensed in Kansas and Missouri
• The choice of an attorney is an important decision and should not be based solely upon advertisement. (in small print along the bottom)
• Add TopCounsel Logo and Finest at Law 2015 Logo
• social media
Should not have
• Cluttered

```html
<!DOCTYPE html>
<html lang="en">
<head>
<meta charset="utf-8">
<title>Haldorsen Law – Estate Planning Ad</title>
<link rel="stylesheet" href="https://fonts.googleapis.com/css2?family=Anton&family=Archivo+Black&family=Cinzel:wght@400;600&family=Lato:wght@400;700;900&display=swap">
<style>
  :root{
    --maroon:#5c0b0e;
    --maroon-light:#7d1216;
    --gold:#96701f;
    --gold-light:#b08a34;
    --black:#0d0b0b;
    --ink:#1c1c1c;
    --paper:#ffffff;
    --backdrop:#e8e3db;
  }
  *{margin:0;padding:0;box-sizing:border-box}
  html,body{width:907px;height:1200px;overflow:hidden;background:var(--backdrop)}
  .ad{position:absolute;left:133px;top:55px;width:640px;height:1090px;background:var(--paper);overflow:hidden;box-shadow:0 6px 18px rgba(0,0,0,.25)}
  .ad-shapes{position:absolute;inset:0;width:640px;height:1090px}
  .t{position:absolute;white-space:nowrap}

  .brand{left:0;width:640px;top:58px;text-align:center;font-family:'Cinzel',serif;font-weight:600;font-size:26px;letter-spacing:2px;color:var(--paper)}
  .brand-dot{display:inline-block;width:12px;height:12px;border-radius:50%;background:var(--paper);margin-right:12px;vertical-align:4px}

  .side{left:0;width:290px;text-align:center;color:var(--paper)}
  .side-title{top:530px;font-family:'Archivo Black',sans-serif;font-size:18px;line-height:22px;letter-spacing:.5px}
  .pill{display:inline-block;background:var(--gold);color:var(--paper);border-radius:12px;padding:1px 12px;font-family:'Archivo Black',sans-serif;font-size:16px;line-height:22px}
  .side-venue-label{top:601px}
  .side-venue{top:628px;font-family:'Cinzel',serif;font-size:19px;line-height:22px}
  .side-services-label{top:694px}
  .side-services{top:725px;font-family:'Lato',sans-serif;font-size:15px;line-height:19px}
  .side-cta{top:853px;font-family:'Archivo Black',sans-serif;font-size:18px;letter-spacing:.5px}
  .side-phone{top:888px;font-family:'Archivo Black',sans-serif;font-size:18px}
  .side-phone svg{vertical-align:-3px;margin-right:6px}

  .headline{left:318px;top:526px;font-family:'Anton',sans-serif;font-size:44px;line-height:52px;color:var(--maroon);letter-spacing:.5px}
  .subhead{left:318px;top:582px;font-family:'Archivo Black',sans-serif;font-size:21px;color:var(--ink)}
  .help-tag{left:300px;top:625px;width:205px;height:36px;background:var(--maroon);border-radius:0 18px 18px 0;color:var(--paper);font-family:'Cinzel',serif;font-size:18px;line-height:36px;padding-left:22px;letter-spacing:.5px}
  .benefits{position:absolute;left:320px;top:680px;width:300px;list-style:none;font-family:'Lato',sans-serif;font-size:15px;line-height:19px;color:var(--ink)}
  .benefits li{position:relative;padding-left:14px;margin-bottom:9px}
  .benefits li::before{content:"";position:absolute;left:0;top:7px;width:6px;height:6px;border-radius:50%;background:var(--maroon)}

  .foot{font-family:'Lato',sans-serif;font-size:15px;line-height:19px;color:var(--paper)}
  .foot-address{left:48px;top:1018px}
  .foot-contact{left:300px;top:1012px}
  .foot svg{position:absolute;left:-16px;top:3px}
  .foot-line{position:relative}
</style>
</head>
<body>
<div class="ad">
  <svg class="ad-shapes" viewBox="0 0 640 1090" xmlns="http://www.w3.org/2000/svg">
    <defs>
      <linearGradient id="photoTone" x1="0" y1="0" x2="0" y2="1">
        <stop offset="0" stop-color="#eef0f1"/>
        <stop offset=".55" stop-color="#c9c6c3"/>
        <stop offset="1" stop-color="#3b3a3d"/>
      </linearGradient>
      <linearGradient id="panelTone" x1="0" y1="0" x2="0" y2="1">
        <stop offset="0" stop-color="#7d1216"/>
        <stop offset="1" stop-color="#4a080b"/>
      </linearGradient>
      <radialGradient id="portraitTone" cx=".5" cy=".45" r=".6">
        <stop offset="0" stop-color="#b9b6b3"/>
        <stop offset="1" stop-color="#4b4d52"/>
      </radialGradient>
      <linearGradient id="headerTone" x1="0" y1="0" x2="0" y2="1">
        <stop offset="0" stop-color="#4a080b"/>
        <stop offset="1" stop-color="#6a0d11"/>
      </linearGradient>
    </defs>

    <path role="img" aria-label="Photo of a smiling team of attorneys gathered around a conference table" d="M0 100 Q320 210 640 110 V470 Q320 440 0 525 Z" fill="url(#photoTone)"/>

    <path d="M0 0 H640 V104 Q320 198 0 96 Z" fill="url(#headerTone)"/>
    <path d="M0 104 Q320 208 640 114" fill="none" stroke="var(--gold)" stroke-width="6"/>

    <path d="M0 530 Q150 482 302 470 Q335 720 278 965 L0 980 Z" fill="url(#panelTone)"/>
    <path d="M0 525 Q320 440 640 470" fill="none" stroke="var(--gold)" stroke-width="8"/>
    <path d="M302 470 Q335 720 278 965" fill="none" stroke="var(--gold)" stroke-width="4"/>

    <path d="M0 970 Q320 925 640 935 V1090 H0 Z" fill="var(--black)"/>
    <path d="M0 966 Q320 921 640 931" fill="none" stroke="var(--gold)" stroke-width="5"/>

    <circle cx="420" cy="935" r="64" fill="var(--paper)"/>
    <circle cx="420" cy="935" r="60" fill="var(--maroon)"/>
    <circle role="img" aria-label="Portrait of attorney Milo T. Haldorsen" cx="420" cy="935" r="56" fill="url(#portraitTone)"/>
    <circle cx="566" cy="970" r="66" fill="var(--paper)"/>
    <circle cx="566" cy="970" r="62" fill="var(--maroon)"/>
    <circle role="img" aria-label="Portrait of a second firm attorney" cx="566" cy="970" r="58" fill="url(#portraitTone)"/>
  </svg>

  <div class="t brand"><span class="brand-dot"></span>HALDORSEN LAW</div>

  <div class="t side side-title">ESTATE PLANNING<br>LAW FIRM</div>
  <div class="t side side-venue-label"><span class="pill">VENU</span></div>
  <div class="t side side-venue">OVERLAND PARK<br>KANSAS</div>
  <div class="t side side-services-label"><span class="pill">OUR SERVICES</span></div>
  <div class="t side side-services">Family Estate Planning -TrussWills<br>Powers of Attorney-Business<br>Succession Planning-Probate &amp; Trust<br>Administration-Asset Protection<br>-Planning-Special Needs</div>
  <div class="t side side-cta">FREE CONSULTATION</div>
  <div class="t side side-phone"><svg width="16" height="16" viewBox="0 0 16 16"><circle cx="8" cy="8" r="7" fill="none" stroke="#fff" stroke-width="1.2"/><path d="M5.5 4.5c-.8.6-.8 2.2.8 4.2s3.4 2.8 4.2 2l.6-.8-1.6-1.2-.8.6c-.6-.2-1.6-1.2-1.9-1.9l.6-.8-1.2-1.6z" fill="#fff"/></svg>(555) 406-7319</div>

  <div class="t headline">WE WILL BE THERE</div>
  <div class="t subhead">WHEN YOU NEED US..</div>
  <div class="t help-tag">LET US HELP YOU</div>
  <ul class="benefits">
    <li>Avoid Probate and Court Interference with Your Affairs</li>
    <li>Minimize Family In-fighting</li>
    <li>Protect Heirs from Wasting Inheritances</li>
    <li>Keep Assets in Your Bloodline</li>
    <li>Preserve and Protect IRA's and Retirement Accounts</li>
  </ul>

  <div class="t foot foot-address">
    <div class="foot-line"><svg width="11" height="11" viewBox="0 0 12 12"><path d="M6 1 L11 6 H9.5 V11 H2.5 V6 H1 Z" fill="var(--gold-light)"/></svg>4820 Pinecrest Avenue Suite</div>
    <div>310 Overland Park</div>
    <div>KS 66000</div>
  </div>
  <div class="t foot foot-contact">
    <div class="foot-line"><svg width="11" height="11" viewBox="0 0 12 12"><circle cx="6" cy="6" r="5" fill="none" stroke="var(--gold-light)" stroke-width="1"/><path d="M4 3.5c-.6.5-.5 1.7.6 3s2.4 2 3 1.4l.4-.6-1.1-.8-.5.4c-.5-.2-1.1-.9-1.3-1.3l.4-.5-.8-1.1z" fill="var(--gold-light)"/></svg>(555) 406-7319</div>
    <div class="foot-line"><svg width="11" height="11" viewBox="0 0 12 12"><circle cx="6" cy="6" r="5" fill="var(--gold-light)"/></svg>www.haldorsenlawkc.com</div>
  </div>
</div>
</body>
</html>
```